Header/Banner Design for Website

Looking for a banner/header design for www.fixerupperdiaries.net Should be fun and whimsical, and include the name of the website, something to do with home improvement or tools, and a caricature of a young, beautiful 20 something blond who the website revolves around. The website is about a young woman who bought her first house and it taking on all of the renovations and remodeling on her own for the first time.

The header/banner should include the same colors that are in the website. The width should be no more than 430 pixels, the height is flexible but the current space in the header is 85 pixels...looking for some creativity. any questions, please ask. Attached an image that she liked for the image of the woman (would like to see versions of this included)
Updates

Target Market(s)

women 20+ that are new home owners or that are tackling home improvement on their own

Industry/Entity Type

Home Improvement

Requirements
Must have
• color coordinate with the website
should feature a young, blond, female caricature
should include the name of the website

```html
<!DOCTYPE html>
<html lang="en">
<head>
<meta charset="utf-8">
<title>Fixer Upper Diaries – Header</title>
<link rel="stylesheet" href="https://fonts.googleapis.com/css2?family=Cinzel:wght@500;700&display=swap">
<style>
  :root {
    --bg-pink: #f3e4ea;
    --bg-pink-deep: #ecd6df;
    --band-pink: #f9d2e3;
    --band-edge: #f3bcd3;
    --crack-grey: #d9cfd3;
    --ornament-grey: #8e8a8c;
    --ornament-soft: #bdb6b9;
    --figure-hair: #f3d77e;
    --figure-shirt: #e9589f;
    --title-dark: #6e1345;
    --title-mid: #a8276c;
    --title-light: #d9559b;
  }

  html, body {
    margin: 0;
    padding: 0;
    overflow: hidden;
    background: #ffffff;
  }

  .site-header {
    position: relative;
    width: 1200px;
    height: 237px;
    overflow: hidden;
    background: linear-gradient(180deg, var(--bg-pink) 0%, var(--bg-pink-deep) 100%);
  }

  .cracked-wall {
    position: absolute;
    left: 640px;
    top: 0;
    width: 560px;
    height: 237px;
    background: radial-gradient(ellipse at 70% 40%, var(--crack-grey) 0%, rgba(217, 207, 211, 0) 70%);
  }

  .accent-band {
    position: absolute;
    left: 0;
    top: 133px;
    width: 1200px;
    height: 32px;
    background: var(--band-pink);
    border-top: 1px solid var(--band-edge);
    border-bottom: 1px solid var(--band-edge);
  }

  .mirror-ornament {
    position: absolute;
    left: 180px;
    top: 4px;
    width: 285px;
    height: 226px;
    border-radius: 50% / 45%;
    background: radial-gradient(ellipse at 50% 45%, rgba(189, 182, 185, 0.25) 0%, rgba(142, 138, 140, 0.55) 60%, rgba(142, 138, 140, 0) 72%);
  }

  .mascot {
    position: absolute;
    left: 4px;
    top: 0;
    width: 158px;
    height: 237px;
    border-radius: 70px 70px 20px 20px;
    background: linear-gradient(180deg, var(--figure-hair) 0%, var(--figure-hair) 38%, var(--figure-shirt) 62%, var(--figure-shirt) 100%);
  }

  .site-title {
    position: absolute;
    left: 0;
    top: 0;
    width: 1200px;
    height: 237px;
  }

  .site-title text {
    font-family: "Cinzel", "Times New Roman", serif;
    font-weight: 700;
    fill: url(#titleFill);
  }

  .title-word-lead { font-size: 104px; }
  .title-word-main { font-size: 82px; }
  .title-word-tail { font-size: 66px; font-weight: 500; }
</style>
</head>
<body>
  <header class="site-header">
    <div class="cracked-wall" role="img" aria-label="Faint cracked plaster texture across the right side"></div>
    <div class="accent-band"></div>
    <div class="mirror-ornament" role="img" aria-label="Grey baroque mirror frame ornament with fluttering butterflies"></div>
    <div class="mascot" role="img" aria-label="Cartoon of a smiling young blonde woman in a pink top holding a hammer"></div>

    <svg class="site-title" viewBox="0 0 1200 237" aria-label="Fixer Upper Diaries">
      <defs>
        <linearGradient id="titleFill" x1="0" y1="0" x2="0" y2="1">
          <stop offset="0" stop-color="var(--title-light)"/>
          <stop offset="0.45" stop-color="var(--title-mid)"/>
          <stop offset="1" stop-color="var(--title-dark)"/>
        </linearGradient>
      </defs>
      <text class="title-word-lead" x="196" y="132" textLength="272" lengthAdjust="spacingAndGlyphs">FIXER</text>
      <text class="title-word-main" x="496" y="132" textLength="676" lengthAdjust="spacing">UPPER</text>
      <text class="title-word-tail" x="516" y="222" textLength="628" lengthAdjust="spacing">DIARIES</text>
    </svg>
  </header>
</body>
</html>
```